Banner Ad to promote Youth Cycling Camps

We need a 728 x 90 banner ad to promote some youth cycling camps. There are 2 different camps - a road camp where they learn to ride their bikes on the roads and a mountain bike camp. The camps teach bike handling skills and racing tactics.

Target Market(s)

Parents of youth ages 7-17

Industry/Entity Type

Non-Profit

Font styles to use
Sans Serif

Requirements
Must have
• Logo
• Dates - Road Camp May 5-7, 2017
• - Mountain Bike Camp July 14-16, 2017
• website - quadrapedalcup.org
• be 728 x 90
Nice to have
• Animated - would like it to rotate with 3 slides - 1 a focus on both camps, 1 on road camp, 1 on mountain bike camp

```html
<!DOCTYPE html>
<html lang="en">
<head>
<meta charset="utf-8">
<title>Youth Cycling Camps Banner</title>
<link rel="stylesheet" href="https://fonts.googleapis.com/css2?family=Oswald:wght@400;500;600&display=swap">
<style>
  :root {
    --ink: #000000;
    --paper: #ffffff;
    --sky: #5bc4ec;
    --lime: #8dc63f;
    --magenta: #e5157f;
    --road-tone-a: #6d6f73;
    --road-tone-b: #2a2b2e;
    --trail-tone-a: #5d6b3e;
    --trail-tone-b: #a39a7c;
    --group-tone-a: #7d8a6a;
    --group-tone-b: #b0a89a;
  }
  * { margin: 0; padding: 0; box-sizing: border-box; }
  html, body { width: 1200px; height: 148px; overflow: hidden; background: var(--ink); }
  .banner {
    position: relative;
    width: 1200px;
    height: 148px;
    background: var(--ink);
    overflow: hidden;
    font-family: "Oswald", "Arial Narrow", sans-serif;
    color: var(--paper);
    text-transform: uppercase;
  }
  .brand {
    position: absolute;
    left: 18px;
    top: 46px;
    width: 62px;
    display: flex;
    flex-direction: column;
    align-items: center;
  }
  .brand-dot {
    width: 46px; height: 46px;
    border-radius: 50%;
    background: var(--sky);
  }
  .brand-name {
    margin-top: 3px;
    font-size: 8px;
    font-weight: 500;
    letter-spacing: 0.3px;
    color: var(--sky);
    white-space: nowrap;
  }
  .headline {
    position: absolute;
    left: 98px;
    width: 232px;
    top: 31px;
    text-align: center;
    line-height: 1;
    white-space: nowrap;
  }
  .headline-top { font-size: 19px; font-weight: 500; letter-spacing: 0.2px; }
  .headline-main { font-size: 28px; font-weight: 500; color: var(--sky); margin-top: 8px; letter-spacing: 0.2px; }
  .headline-ages { font-size: 13px; font-weight: 500; margin-top: 8px; letter-spacing: 0.6px; }

  .photo {
    position: absolute;
    top: 0;
    height: 148px;
  }
  .photo-road { left: 362px; width: 162px; background: linear-gradient(160deg, var(--road-tone-a), var(--road-tone-b)); }
  .photo-trail { left: 524px; width: 164px; background: linear-gradient(180deg, var(--trail-tone-a), var(--trail-tone-b)); }
  .photo-group { left: 688px; width: 188px; background: linear-gradient(180deg, var(--group-tone-a), var(--group-tone-b)); }
  .photo-label {
    position: absolute;
    top: 86px;
    left: 50%;
    transform: translateX(-50%);
    background: var(--ink);
    padding: 2px 9px;
    font-size: 11.5px;
    font-weight: 500;
    letter-spacing: 0.4px;
    white-space: nowrap;
  }

  .frame-lines { position: absolute; inset: 0; pointer-events: none; }

  .info {
    position: absolute;
    left: 916px;
    top: 20px;
    width: 270px;
    white-space: nowrap;
  }
  .schedule {
    font-size: 15px;
    font-weight: 400;
    line-height: 1;
    letter-spacing: 0.3px;
  }
  .schedule-item + .schedule-item { margin-top: 12px; }
  .contact {
    margin-top: 14px;
    display: flex;
    align-items: center;
    gap: 14px;
  }
  .contact-icon { width: 26px; height: 26px; }
  .contact-number { font-size: 22px; font-weight: 400; letter-spacing: 0.4px; line-height: 1; }
  .website {
    margin-top: 12px;
    font-size: 14px;
    font-weight: 500;
    letter-spacing: 0.6px;
    color: var(--sky);
    text-transform: lowercase;
    line-height: 1;
  }
</style>
</head>
<body>
<div class="banner">

  <div class="brand">
    <div class="brand-dot"></div>
    <div class="brand-name">Quadrapedal Cup</div>
  </div>

  <div class="headline">
    <div class="headline-top">Best Cycling</div>
    <div class="headline-main">Camps for Youth</div>
    <div class="headline-ages">Ages 7-17</div>
  </div>

  <div class="photo photo-road" role="img" aria-label="Young rider on a road bike in black kit">
    <span class="photo-label">Road Camp</span>
  </div>
  <div class="photo photo-trail" role="img" aria-label="Youth mountain biker riding a forest trail">
    <span class="photo-label">Mountain Camp</span>
  </div>
  <div class="photo photo-group" role="img" aria-label="Group of young cyclists riding together on a dirt road">
    <span class="photo-label">Cycling Camps</span>
  </div>

  <svg class="frame-lines" width="1200" height="148" viewBox="0 0 1200 148" aria-hidden="true">
    <polygon points="0,132 0,148 16,148" fill="var(--lime)"/>
    <polygon points="1182,0 1200,0 1200,18" fill="var(--magenta)"/>
    <polygon points="326,136 332,132 332,140" fill="var(--sky)"/>
    <polygon points="334,136 340,132 340,140" fill="var(--sky)"/>
    <polygon points="342,136 348,132 348,140" fill="var(--sky)"/>
    <polygon points="350,136 356,132 356,140" fill="var(--sky)"/>
    <polyline points="362,0 362,108 352,116 362,124 362,148" fill="none" stroke="var(--sky)" stroke-width="3"/>
    <line x1="524" y1="0" x2="524" y2="148" stroke="var(--ink)" stroke-width="2"/>
    <line x1="688" y1="0" x2="688" y2="148" stroke="var(--ink)" stroke-width="2"/>
    <polyline points="876,0 876,60 888,72 876,84 876,148" fill="var(--ink)" stroke="var(--sky)" stroke-width="3"/>
  </svg>

  <div class="info">
    <div class="schedule">
      <div class="schedule-item">Road Camp — May 5-7, 2017</div>
      <div class="schedule-item">Mountain Bike Camp — July 14-16, 2017</div>
    </div>
    <div class="contact">
      <svg class="contact-icon" viewBox="0 0 24 24" aria-hidden="true">
        <path fill="var(--sky)" d="M6.6 10.8a15.1 15.1 0 0 0 6.6 6.6l2.2-2.2a1 1 0 0 1 1-.25 11.4 11.4 0 0 0 3.6.57 1 1 0 0 1 1 1V20a1 1 0 0 1-1 1A17 17 0 0 1 3 4a1 1 0 0 1 1-1h3.5a1 1 0 0 1 1 1c0 1.25.2 2.45.57 3.57a1 1 0 0 1-.25 1z"/>
      </svg>
      <span class="contact-number">+1 303-555-0142</span>
    </div>
    <div class="website">quadrapedalcup.org</div>
  </div>

</div>
</body>
</html>
```